Tending the Hidden Garden; A Map Toward Calm, Purpose & Belonging

I need a book cover, for the above book title. This is a journey of the heart to know the heart of God. I think on the text, Simple (see below graphic)
Black Lettering for Tending.....Garden
Gold lettering for God
Either gold or black for the subtitle; A Map Toward Calm, Purpose, & Belonging
I would like the below graphic idea only no photograph of a person,
and White background instead of black
Simple Font, like below graphic, but open to suggestions

not age specific, Every person has been given a heart to know God, we are taking the mystery out the process to understand God is Father, loving gracious, ever present, etc. If we know His heart, we realize He's not at a distance, He is there, an ever present help

Security

• Title: Tending the Hidden Garden; A Map Toward Calm, Purpose, & Belonging
• My name, Rob Fenwick
• See Below Graphic

```html
<!DOCTYPE html>
<html lang="en">
<head>
<meta charset="UTF-8">
<title>Tending the Hidden Garden — Rob Fenwick</title>
<link href="https://fonts.googleapis.com/css2?family=Josefin+Sans:wght@400;600&family=Montserrat:wght@500;700;800;900&display=swap" rel="stylesheet">
<style>
  :root {
    --backdrop: #d9d9d9;
    --paper: #ffffff;
    --ink: #111111;
    --gold-light: #f7c26a;
    --gold-mid: #e08a1e;
    --gold-deep: #8a3c08;
    --rule-gold: #e3a53a;
    --sparkle: rgba(232, 205, 160, 0.35);
  }
  * { margin: 0; padding: 0; box-sizing: border-box; }
  html, body {
    width: 1200px;
    height: 900px;
    overflow: hidden;
    background: var(--backdrop);
  }
  .book-cover {
    position: absolute;
    left: 277px;
    top: 0;
    width: 646px;
    height: 900px;
    background: var(--paper);
    overflow: hidden;
  }
  .sparkle-field {
    position: absolute;
    left: 180px;
    top: 110px;
    width: 300px;
    height: 640px;
    background:
      radial-gradient(circle at 50% 10%, var(--sparkle) 0, transparent 60px),
      radial-gradient(circle at 30% 18%, var(--sparkle) 0, transparent 40px),
      radial-gradient(circle at 75% 22%, var(--sparkle) 0, transparent 35px),
      radial-gradient(circle at 55% 90%, var(--sparkle) 0, transparent 70px),
      radial-gradient(circle at 35% 78%, var(--sparkle) 0, transparent 40px);
  }
  .author {
    position: absolute;
    left: 97px;
    top: 52px;
    width: 448px;
    text-align: center;
  }
  .author .rule {
    display: block;
    height: 2px;
    background: linear-gradient(90deg, var(--gold-mid), var(--rule-gold), var(--gold-mid));
  }
  .author-name {
    font-family: "Montserrat", sans-serif;
    font-weight: 800;
    font-size: 30px;
    letter-spacing: 0.42em;
    padding-left: 0.42em;
    color: var(--ink);
    line-height: 40px;
    margin: 2px 0;
  }
  .title {
    position: absolute;
    left: 0;
    top: 240px;
    width: 646px;
    text-align: center;
    color: var(--ink);
  }
  .title span { display: block; }
  .title-lead {
    font-family: "Josefin Sans", sans-serif;
    font-weight: 600;
    font-size: 78px;
    letter-spacing: 0.08em;
    line-height: 84px;
  }
  .title-link {
    font-family: "Josefin Sans", sans-serif;
    font-weight: 600;
    font-size: 30px;
    letter-spacing: 0.5em;
    padding-left: 0.5em;
    line-height: 40px;
  }
  .title-key {
    font-family: "Montserrat", sans-serif;
    font-weight: 900;
    font-size: 128px;
    letter-spacing: -0.03em;
    line-height: 140px;
    background: linear-gradient(90deg, var(--gold-deep) 0%, var(--gold-mid) 25%, var(--gold-light) 50%, var(--gold-mid) 75%, var(--gold-deep) 100%);
    -webkit-background-clip: text;
    background-clip: text;
    color: transparent;
  }
  .title-end {
    font-family: "Montserrat", sans-serif;
    font-weight: 900;
    font-size: 96px;
    letter-spacing: 0.01em;
    line-height: 100px;
  }
  .subtitle {
    position: absolute;
    left: 0;
    top: 780px;
    width: 646px;
    text-align: center;
    color: var(--ink);
    font-family: "Montserrat", sans-serif;
  }
  .subtitle-lead {
    display: block;
    font-weight: 500;
    font-size: 19px;
    letter-spacing: 0.72em;
    padding-left: 0.72em;
    line-height: 26px;
  }
  .subtitle-themes {
    display: block;
    font-weight: 800;
    font-size: 24px;
    line-height: 32px;
  }
</style>
</head>
<body>
  <main class="book-cover">
    <div class="sparkle-field" role="img" aria-label="Scattered soft golden sparkles and starbursts"></div>

    <header class="author">
      <span class="rule"></span>
      <p class="author-name">ROB FENWICK</p>
      <span class="rule"></span>
    </header>

    <h1 class="title">
      <span class="title-lead">TENDING</span>
      <span class="title-link">THE</span>
      <span class="title-key">HIDDEN</span>
      <span class="title-end">GARDEN</span>
    </h1>

    <p class="subtitle">
      <span class="subtitle-lead">A MAP TOWARD</span>
      <span class="subtitle-themes">CALM, PURPOSE, &amp; BELONGING</span>
    </p>
  </main>
</body>
</html>
```